I LOVE BRISA LOMA

I would like a one page site that links to my real estate team website. Brisa Loma is a upscale and diverse subdivision in Bethesda Maryland about 30 minutes from downtown DC.
I am thinking of a modern Dunwick w/ a global-hip look.
We have T-Ball, Soccer, bike trails, bunnies, dogs and cats, bee-keepers, farmer markets, GREAT PUBLIC SCHOOLS
kids, kids, kids
I live in this area and love it and want to sell more houses here so I want this webpage to link to my site but be unique to this subdivision.

Target Market(s)

real estate - home sellers and home buyers

Industry/Entity Type

Real Estate Agent

Coding

Coded - Design and coding required

Number of Pages Required

1 page

Font styles to use
Sans Serif

Requirements
Must have
• Clear message The Corwin & Mirela Team sells in Brisa Loma
Nice to have
• Images that reflect the fantastic Modern Dunwick meet hip Global world feel

```html
<!DOCTYPE html>
<html lang="en">
<head>
<meta charset="utf-8">
<title>I Love Brisa Loma</title>
<link rel="stylesheet" href="https://fonts.googleapis.com/css2?family=Raleway:wght@400;500;600;700;800&family=Playfair+Display:ital,wght@1,700&display=swap">
<style>
:root{
  --red:#e8263f;
  --teal:#6ecfcc;
  --purple:#9866c3;
  --ink:#333333;
  --muted:#7a7a7a;
  --line:#e2e2e2;
  --footer:#3d3d3d;
  --white:#ffffff;
  --logo:#a3122a;
}
*{box-sizing:border-box;margin:0;padding:0}
html,body{width:1200px;height:3636px;overflow:hidden}
body{font-family:"Raleway",Arial,sans-serif;color:var(--ink);background:var(--white);position:relative}
.abs{position:absolute}
.img-fill{position:absolute}
.btn{display:inline-block;background:var(--red);color:var(--white);font-weight:700;text-transform:uppercase;letter-spacing:.5px}
.btn-ghost{display:inline-block;background:var(--white);color:var(--ink);font-size:11px;font-weight:700;padding:8px 18px;text-transform:uppercase}
.script{font-family:"Playfair Display",Georgia,serif;font-style:italic;font-weight:700}

/* header */
.site-header{left:0;top:0;width:1200px;height:98px;background:var(--teal)}
.logo{left:200px;top:8px;width:380px;text-align:center}
.logo-dot{width:40px;height:40px;border-radius:50%;background:var(--red);margin:0 auto 6px}
.logo-name{font-size:28px;font-weight:800;color:var(--logo);letter-spacing:1px;white-space:nowrap}
.main-nav{left:568px;top:30px;display:flex;list-style:none;align-items:center}
.main-nav li{font-size:13px;font-weight:600;color:var(--white);padding:12px 24px}
.main-nav li.active{background:var(--red)}
.search-icon{margin-left:6px}

/* hero */
.hero{left:0;top:98px;width:1200px;height:522px;background:linear-gradient(120deg,#8d9a9a 0%,#c9a079 30%,#d2763f 55%,#b9894f 75%,#7c8560 100%)}
.hero-text{right:90px;top:130px;width:600px;text-align:right;color:var(--white)}
.hero-kicker{font-size:22px;font-weight:800;letter-spacing:1px}
.hero-title{font-size:68px;line-height:1.1;color:#f4e4d4;margin:6px 0 6px}
.hero-lead{font-size:19px;font-weight:700;line-height:1.35}
.hero .btn{font-size:17px;padding:14px 34px;margin-top:28px;margin-right:100px}
.hero-arrow{top:340px;width:16px;height:28px}
.hero-dots{left:560px;top:582px;display:flex;gap:8px}
.hero-dots span{width:9px;height:9px;border-radius:50%;background:rgba(255,255,255,.6)}
.hero-dots span.on{background:var(--white)}

/* contact bar */
.contact-bar{left:0;top:620px;width:1200px;height:77px;border-bottom:1px solid var(--line);display:flex;align-items:center;justify-content:space-between;padding:0 50px 0 78px;font-size:15px;color:var(--muted)}
.contact-item{display:flex;align-items:center;gap:12px}

/* feature grid */
.feature-grid{left:0;top:697px;width:1200px;height:715px;display:grid;grid-template-columns:400px 400px 400px;grid-template-rows:357px 358px}
.tile{position:relative;color:var(--white);text-align:center;padding:60px 40px 0}
.tile-teal{background:var(--teal)}
.tile-purple{background:var(--purple)}
.tile-red{background:var(--red)}
.tile h2{font-size:34px;margin-bottom:10px}
.tile .rule{width:60px;height:10px;margin:0 auto 18px}
.tile p{font-size:15px;font-weight:600;line-height:1.35;margin-bottom:26px}

/* testimonial */
.testimonial{left:176px;top:1540px;width:845px;height:263px;background:var(--white);box-shadow:0 1px 4px rgba(0,0,0,.15)}
.testimonial-photo{left:0;top:0;width:424px;height:263px;background:linear-gradient(135deg,#6f9b3e,#a9c46b 50%,#5f8a34)}
.testimonial-body{left:456px;top:36px;width:360px}
.testimonial-body h3{font-size:19px;font-weight:800;text-transform:uppercase;margin:12px 0 10px}
.testimonial-body p{font-size:15px;color:var(--muted);line-height:1.4}
.testimonial-body .author{color:var(--red);font-size:12px;font-weight:700;text-transform:uppercase;margin-top:14px}
.t-dots{left:566px;top:1826px;display:flex;gap:8px}
.t-dots span{width:9px;height:9px;border-radius:50%;background:#c7c7c7}
.t-dots span.on{background:#555}

/* three widgets */
.widget h4{font-size:20px;font-weight:800;text-transform:uppercase;margin-bottom:18px}
.events{left:176px;top:1910px;width:270px}
.event-tabs{display:flex;height:32px}
.event-tabs span{flex:1;text-align:center;font-size:11px;font-weight:700;line-height:32px;background:#eeeeee;color:var(--muted)}
.event-tabs span.on{background:var(--red);color:var(--white)}
.event-body{border:1px solid var(--line);border-top:0;padding:16px;display:flex;gap:12px;height:200px}
.event-thumb{width:90px;height:70px;flex:none;background:linear-gradient(135deg,#b2a08c,#6f655c)}
.event-body p{font-size:12px;color:var(--muted);line-height:1.35}

.accordion{left:470px;top:1910px;width:270px}
.acc-item{border:1px solid var(--line);height:40px;display:flex;justify-content:space-between;align-items:center;padding:0 12px;font-size:11px;font-weight:700;text-transform:uppercase;margin-bottom:6px}
.acc-item.open{background:var(--purple);color:var(--white);border-color:var(--purple);margin-bottom:0}
.acc-panel{border:1px solid var(--line);border-top:0;padding:14px;display:flex;gap:12px;height:118px;margin-bottom:6px;overflow:hidden}
.acc-thumb{width:70px;height:84px;flex:none;background:linear-gradient(135deg,#8a7a6c,#3f3a36)}
.acc-panel p{font-size:12px;color:var(--muted);line-height:1.3}
.plus{color:var(--red);font-size:20px;font-weight:500}
.acc-item.open .plus{color:var(--white)}

.gallery{left:758px;top:1910px;width:266px}
.gallery-photo{position:relative;width:266px;height:220px;background:linear-gradient(135deg,#c95a4a,#e7b4a0 45%,#8c3a33)}
.gallery-bar{position:absolute;left:0;bottom:0;width:266px;height:30px;background:var(--teal);display:flex;justify-content:space-around;align-items:center}

/* blog */
.blog{left:0;top:2310px;width:1200px;height:387px}
.blog-img{top:0;height:211px}
.date-badge{position:absolute;left:18px;top:0;width:46px;height:56px;background:var(--purple);color:var(--white);text-align:center}
.date-badge b{display:block;font-size:20px;padding-top:6px}
.date-badge small{font-size:10px}
.blog-post{top:236px;width:360px}
.blog-post h3{font-size:19px;font-weight:800;text-transform:uppercase;margin-bottom:10px}
.blog-post p{font-size:13px;color:var(--muted);line-height:1.35;margin-bottom:14px}
.blog-post .btn{font-size:11px;padding:6px 14px}

/* map + form */
.map{left:0;top:2697px;width:1200px;height:621px;background:linear-gradient(135deg,#e6e4dc,#d9dccc 40%,#e3e0d6 70%,#cfd6d8)}
.contact-card{left:176px;top:2945px;width:845px;height:343px;background:var(--white);box-shadow:0 1px 5px rgba(0,0,0,.18)}
.contact-form{left:36px;top:24px;width:360px}
.contact-form h3{font-size:17px;font-weight:800;text-transform:uppercase;margin:12px 0 16px;white-space:nowrap}
.field-row{display:flex;gap:12px;margin-bottom:14px}
.field{height:30px;flex:1;border:2px solid var(--line);font-size:11px;color:#aaa;padding:6px 8px}
.field.focus{border-color:var(--teal)}
.field.area{height:90px;flex:none;width:100%;border-width:3px;border-color:#bbb}
.contact-form .btn{font-size:12px;padding:8px 16px;margin-top:14px}
.contact-photo{left:424px;top:0;width:421px;height:343px;background:linear-gradient(160deg,#2b2f34,#5b4b35 50%,#1c2024)}

/* footer */
.site-footer{left:0;top:3318px;width:1200px;height:318px;background:var(--footer);color:var(--white)}
.footer-logo{left:166px;top:28px;width:270px;text-align:center}
.footer-logo .logo-dot{width:34px;height:34px}
.footer-logo .logo-name{font-size:22px;color:var(--white)}
.footer-about{left:176px;top:112px;width:270px;font-size:12px;line-height:1.35}
.footer-copy{left:176px;top:270px;font-size:11px;line-height:1.4}
.footer-social{left:470px;top:8px}
.footer-social h5,.footer-contact h5{font-size:13px;font-weight:800;text-transform:uppercase;margin-bottom:10px}
.feed-box{width:240px;height:140px;background:var(--white);padding:10px;color:var(--ink)}
.feed-head{display:flex;gap:8px;align-items:center;font-size:12px;font-weight:700}
.feed-sq{width:30px;height:30px;background:#5a6f9a}
.feed-row{display:flex;gap:4px;margin-top:44px}
.feed-row span{width:24px;height:24px;background:#c8c8c8}
.footer-contact{left:758px;top:46px;width:300px}
.footer-contact p{font-size:12px;line-height:1.5}
.social-icons{left:176px;top:164px;display:flex;gap:6px}
.social-icons span{width:28px;height:28px;background:var(--red)}
.back-top{right:146px;top:282px;font-size:12px;display:flex;align-items:center;gap:8px}
</style>
</head>
<body>

<header class="abs site-header">
  <div class="abs logo">
    <div class="logo-dot"></div>
    <div class="logo-name">I LOVE BRISA LOMA</div>
  </div>
  <ul class="abs main-nav">
    <li class="active">Home</li>
    <li>About Us</li>
    <li>Blog</li>
    <li>Gallery</li>
    <li>Contact</li>
    <li class="search-icon"><svg width="14" height="14" viewBox="0 0 14 14"><circle cx="6" cy="6" r="4.5" fill="none" stroke="#fff" stroke-width="1.6"/><line x1="9.5" y1="9.5" x2="13" y2="13" stroke="#fff" stroke-width="1.6"/></svg></li>
  </ul>
</header>

<section class="abs hero">
  <div class="img-fill" role="img" aria-label="Autumn street scene with a passing commuter train and a tree in orange leaves" style="inset:0"></div>
  <svg class="abs hero-arrow" style="left:14px" viewBox="0 0 16 28"><polyline points="12,4 4,14 12,24" fill="none" stroke="#fff" stroke-width="3"/></svg>
  <svg class="abs hero-arrow" style="right:14px" viewBox="0 0 16 28"><polyline points="4,4 12,14 4,24" fill="none" stroke="#fff" stroke-width="3"/></svg>
  <div class="abs hero-text">
    <div class="hero-kicker">I LOVE BRISA LOMA</div>
    <div class="hero-title script">Welcome</div>
    <p class="hero-lead">The Corwin &amp; Mirela Team sells homes<br>in Brisa Loma, your neighborhood experts</p>
    <span class="btn">Read more</span>
  </div>
  <div class="abs hero-dots"><span></span><span class="on"></span><span></span><span></span><span></span></div>
</section>

<div class="abs contact-bar">
  <div class="contact-item">
    <svg width="22" height="18" viewBox="0 0 22 18"><rect x="1" y="1" width="20" height="16" fill="none" stroke="#e8263f" stroke-width="2"/><polyline points="1,1 11,10 21,1" fill="none" stroke="#e8263f" stroke-width="2"/></svg>
    hello@brisaloma-homes.com
  </div>
  <div class="contact-item">
    <svg width="14" height="22" viewBox="0 0 14 22"><rect x="1" y="1" width="12" height="20" rx="2" fill="none" stroke="#e8263f" stroke-width="2"/><circle cx="7" cy="17" r="1.3" fill="#e8263f"/></svg>
    +1 555 01 234-567
  </div>
  <div class="contact-item">
    <svg width="20" height="20" viewBox="0 0 20 20"><polygon points="2,9 18,2 11,18 9,11" fill="none" stroke="#e8263f" stroke-width="2" stroke-linejoin="round"/></svg>
    1482 Larkmoor Street NW, Washington, DC
  </div>
</div>

<section class="abs feature-grid">
  <div class="tile tile-teal">
    <h2 class="script">Join Us</h2>
    <svg class="rule" viewBox="0 0 60 10"><line x1="0" y1="3" x2="60" y2="3" stroke="#fff"/><line x1="10" y1="7" x2="50" y2="7" stroke="#fff"/></svg>
    <p>Contact The Corwin &amp; Mirela Team today to learn more about how you can join us and others working towards the betterment of your community.</p>
    <span class="btn-ghost">See more</span>
  </div>
  <div class="img-fill" role="img" aria-label="Family playing together in a flower meadow under a blue sky" style="position:relative;background:linear-gradient(180deg,#7fb3e0 0%,#bcd7ee 45%,#c0483a 70%,#6e8f3a 100%)"></div>
  <div class="tile tile-purple">
    <h2 class="script">Lorem Ipsum</h2>
    <svg class="rule" viewBox="0 0 60 10"><line x1="0" y1="3" x2="60" y2="3" stroke="#fff"/><line x1="10" y1="7" x2="50" y2="7" stroke="#fff"/></svg>
    <p>Lorem ipsum dolor sit amet, consectetur dipisicing elit, sed do eiusmod tempor incididunt ut labore et dolore.</p>
    <span class="btn-ghost">See more</span>
  </div>
  <div class="img-fill" role="img" aria-label="Mother carrying her baby in a front carrier outdoors" style="position:relative;background:linear-gradient(135deg,#6f8f4a,#b7c98a 50%,#4f6b34)"></div>
  <div class="tile tile-red">
    <h2 class="script">Better Life</h2>
    <svg class="rule" viewBox="0 0 60 10"><line x1="0" y1="3" x2="60" y2="3" stroke="#fff"/><line x1="10" y1="7" x2="50" y2="7" stroke="#fff"/></svg>
    <p>Lorem ipsum dolor sit amet, consectetur dipisicing elit,sed do eiusmod tempor incididunt ut labore et dolore, consectetur adipiscing elit, sed do eipor.</p>
    <span class="btn-ghost">See more</span>
  </div>
  <div class="img-fill" role="img" aria-label="Couple walking bicycles along a sunny country path" style="position:relative;background:linear-gradient(135deg,#e9d3a0,#c9a466 50%,#7d6a3e)"></div>
</section>

<article class="abs testimonial">
  <div class="abs testimonial-photo" role="img" aria-label="Smiling young couple holding their baby on a lawn"></div>
  <div class="abs testimonial-body">
    <svg width="34" height="20" viewBox="0 0 34 20"><path d="M2 18V8l6-6h2L6 8h4v10z M18 18V8l6-6h2l-4 6h4v10z" fill="none" stroke="#e8263f" stroke-width="1.5"/></svg>
    <h3>What other say about us</h3>
    <p>Lorem ipsum dolor sit amet, consectetur dipisicing elit, sed do eiusmod tempor incididunt ut labore et dolore, consectetur adipiscing elit, sed do eipor.</p>
    <div class="author">Dale Morrow</div>
  </div>
</article>
<div class="abs t-dots"><span></span><span class="on"></span><span></span><span></span></div>

<section class="abs widget events">
  <h4>Next events</h4>
  <div class="event-tabs"><span class="on">JAN</span><span>MAY</span><span>AUG</span></div>
  <div class="event-body">
    <div class="event-thumb" role="img" aria-label="Woman reading at a community event"></div>
    <p>Lorem ipsum dolor sit amet, consectetur adipiscing elit, sed do eiusmod tempor incididunt ut labore et dolore magna aliqua minim ad veniam.</p>
  </div>
</section>

<section class="abs widget accordion">
  <h4>Accordion</h4>
  <div class="acc-item">Accordion one <span class="plus">+</span></div>
  <div class="acc-item open">Accordion two <span class="plus">&minus;</span></div>
  <div class="acc-panel">
    <div class="acc-thumb" role="img" aria-label="Neighbor portrait in soft light"></div>
    <p>Lorem ipsum dolor sit amet, consectetur adipiscing elit, sed do eiusmod tempor incididunt ut labore magna aliqua.</p>
  </div>
  <div class="acc-item">Accordion three <span class="plus">+</span></div>
</section>

<section class="abs widget gallery">
  <h4>Image gallery</h4>
  <div class="gallery-photo" role="img" aria-label="Young woman leaning on a red vintage car">
    <div class="gallery-bar">
      <svg width="12" height="12" viewBox="0 0 12 12"><polygon points="10,1 2,6 10,11" fill="none" stroke="#fff" stroke-width="1.5"/></svg>
      <svg width="12" height="12" viewBox="0 0 12 12"><polygon points="2,1 10,6 2,11" fill="none" stroke="#fff" stroke-width="1.5"/></svg>
    </div>
  </div>
</section>

<section class="abs blog">
  <div class="abs blog-img" role="img" aria-label="City street with apartment buildings and parked cars" style="left:0;width:396px;background:linear-gradient(160deg,#9fb8cf,#6c7b86 55%,#3f4a52)">
    <div class="date-badge"><b>12</b><small>Sep</small></div>
  </div>
  <div class="abs blog-img" role="img" aria-label="Little child lying on the grass" style="left:402px;width:396px;background:linear-gradient(160deg,#cfe0a6,#9fbd5e 55%,#5f7f2e)">
    <div class="date-badge"><b>30</b><small>Sep</small></div>
  </div>
  <div class="abs blog-img" role="img" aria-label="Modern family home with pitched roof and trees" style="left:804px;width:396px;background:linear-gradient(160deg,#b9cfe2,#8c8a80 55%,#4e5a3e)">
    <div class="date-badge"><b>05</b><small>Oct</small></div>
  </div>
  <div class="abs blog-post" style="left:30px">
    <h3>Blog title one</h3>
    <p>Lorem ipsum dolor sit amet, consectetur adipiscing elit, sed do eiusmod tempor incidid, consectetur adipiscing elit, sed do eiusmod ut labore et dolore magna aliqua. Ut enim ad minim.</p>
    <span class="btn">Read more</span>
  </div>
  <div class="abs blog-post" style="left:432px">
    <h3>Blog title two</h3>
    <p>Lorem ipsum dolor sit amet, consectetur adipiscing elit, sed do eiusmod tempor incidid, consectetur adipiscing elit, sed do eiusmod ut labore et dolore magna aliqua. Ut enim ad minim.</p>
    <span class="btn">Read more</span>
  </div>
  <div class="abs blog-post" style="left:830px">
    <h3>Blog title three</h3>
    <p>Lorem ipsum dolor sit amet, consectetur adipiscing elit, sed do eiusmod tempor incidid, consectetur adipiscing elit, sed do eiusmod ut labore et dolore magna aliqua. Ut enim ad minim.</p>
    <span class="btn">Read more</span>
  </div>
</section>

<section class="abs map" role="img" aria-label="Street map of the neighborhood and surrounding area"></section>
<section class="abs contact-card">
  <form class="abs contact-form">
    <svg width="22" height="18" viewBox="0 0 22 18"><rect x="1" y="1" width="20" height="16" fill="none" stroke="#e8263f" stroke-width="2"/><polyline points="1,1 11,10 21,1" fill="none" stroke="#e8263f" stroke-width="2"/></svg>
    <h3>Write to us. Will be glad to read</h3>
    <div class="field-row"><div class="field focus">Jack</div><div class="field">Enter your email</div></div>
    <div class="field area">Your message</div>
    <span class="btn">Send</span>
  </form>
  <div class="abs contact-photo" role="img" aria-label="Evening street with shop windows and trees"></div>
</section>

<footer class="abs site-footer">
  <div class="abs footer-logo">
    <div class="logo-dot"></div>
    <div class="logo-name">I LOVE BRISA LOMA</div>
  </div>
  <p class="abs footer-about">The Corwin &amp; Mirela Team sells homes in Brisa Loma, sed do eiusmod tempor elit.</p>
  <div class="abs social-icons"><span></span><span></span><span></span><span></span></div>
  <p class="abs footer-copy">Copyright &copy; I LOVE BRISA LOMA. All rights reserved</p>
  <div class="abs footer-social">
    <h5>Neighbors Feed</h5>
    <div class="feed-box">
      <div class="feed-head"><span class="feed-sq"></span>I Love Brisa Loma</div>
      <div class="feed-row"><span></span><span></span><span></span><span></span><span></span><span></span><span></span></div>
    </div>
  </div>
  <div class="abs footer-contact">
    <h5>Contact us</h5>
    <p>Address: 1482 Larkmoor Street NW,<br>Washington, DC<br>Email: hello@brisaloma-homes.com<br>Tel: +1 555 01 234-567</p>
  </div>
  <div class="abs back-top">Back to top
    <svg width="14" height="12" viewBox="0 0 14 12"><polygon points="7,1 13,11 1,11" fill="none" stroke="#fff" stroke-width="1.5"/></svg>
  </div>
</footer>

</body>
</html>
```